SnackHarbor!!! A Vending Machine Business Looking for an attractive website.

We are a vending machine business in Northern Michigan. We have changed our name and have rebranded our company. We would like an attractive website that shares who we are, what services we provide, the products we offer in our machines, along with a form businesses can fill out to see if they are a good fit for our company. I would like to have a Home Page, About SnackHarbor, Why Choose SnackHarbor?, Products & Services, Contact Us (With a Login Option), and a page with a questionnaire for thos interested in getting a FREE Vending Machine.

Target Market(s)

Businesses, Campgrounds, Schools, and many more in Northern Michigan

Industry/Entity Type

Vending Machines

Number of Pages Required

5+ page

Requirements
Must have
• An inviting and enticing Home Page. I want to get my potential clients engaged in our website.
Nice to have
• Possibly background photos from Northern Michigan
Should not have
• A corporate feel. I do not want a boring website.

```html
<!DOCTYPE html>
<html lang="en">
<head>
<meta charset="utf-8">
<title>SnackHarbor – Crave. Vend. Repeat.</title>
<link href="https://fonts.googleapis.com/css2?family=Rokkitt:wght@600;700;800&family=Barlow:wght@400;500;600&display=swap" rel="stylesheet">
<style>
:root{
  --navy:#1c1d5c;
  --navy-deep:#15164a;
  --green:#2b5a2a;
  --green-dark:#234a22;
  --white:#ffffff;
  --ink:#2a2a3a;
  --muted:#6b6b7a;
  --line:#c9c9d6;
  --field:#ffffff;
}
*{box-sizing:border-box;margin:0;padding:0}
html,body{width:1200px;height:4307px;overflow:hidden}
body{position:relative;background:var(--white);font-family:"Barlow",sans-serif;color:var(--ink)}
.abs{position:absolute}
.heading{font-family:"Rokkitt",serif;font-weight:800;letter-spacing:1px;text-transform:uppercase;white-space:nowrap}
.btn{position:absolute;display:flex;align-items:center;justify-content:center;border-radius:30px;font-family:"Barlow",sans-serif;font-weight:600;font-size:15px;letter-spacing:1px;text-transform:uppercase;color:var(--white);white-space:nowrap}
.btn-green{background:var(--green)}
.btn-navy{background:var(--navy)}
.btn-outline{border:2px solid var(--white)}

/* header */
.site-header{top:0;left:0;width:1200px;height:80px;background:var(--white)}
.brand{font-family:"Rokkitt",serif;font-weight:800;font-size:44px;color:var(--navy);display:flex;align-items:center;gap:8px;white-space:nowrap}
.brand-mark{width:16px;height:16px;background:var(--green)}
.main-nav a{position:absolute;top:27px;font-family:"Rokkitt",serif;font-weight:700;font-size:13px;line-height:12px;color:var(--navy);text-decoration:none;text-transform:uppercase}
.main-nav .sep{position:absolute;top:26px;width:1px;height:28px;background:var(--line)}
.login{left:948px;top:22px;width:103px;height:33px;background:var(--green);border-radius:3px;font-family:"Rokkitt",serif;font-weight:700;font-size:15px;color:var(--white);display:flex;align-items:center;justify-content:center}

/* hero */
.hero{top:80px;left:0;width:1200px;height:680px}
.hero-title{left:97px;top:242px;font-size:66px;color:var(--white);line-height:1}
.hero-sub{left:98px;top:320px;font-size:42px;color:var(--white);line-height:1}
.hero-tag{left:104px;top:385px;font-size:27px;font-weight:500;line-height:31px;color:var(--white);text-transform:uppercase}

/* about */
.about-title{left:630px;top:876px;font-size:44px;line-height:1;letter-spacing:0;color:var(--navy)}
.about-text{left:632px;top:960px;width:520px;font-size:19px;line-height:31px;color:var(--ink)}

/* why */
.why-title{left:0;width:1200px;top:1465px;text-align:center;font-size:48px;line-height:1;color:var(--white)}
.why-rule{left:564px;top:1522px;width:72px;height:3px;background:var(--white)}
.why-text{left:235px;width:730px;top:1546px;text-align:center;font-size:18px;line-height:26px;color:var(--white)}

/* products */
.products-title{left:0;width:1200px;top:2112px;text-align:center;font-size:44px;line-height:1;color:var(--navy)}
.products-rule{left:552px;top:2166px;width:82px;height:3px;background:var(--navy)}
.card{position:absolute;top:2210px;width:270px;height:415px;border:1.5px solid var(--line);border-radius:12px;background:var(--white);overflow:hidden}
.card .photo{position:absolute;left:60px;top:28px;width:150px;height:215px;border-radius:4px}
.card h3{position:absolute;left:0;width:100%;top:266px;text-align:center;font-family:"Rokkitt",serif;font-weight:800;font-size:20px;color:var(--navy);letter-spacing:.5px;white-space:nowrap}
.card p{position:absolute;left:20px;width:230px;top:297px;text-align:center;font-size:12px;line-height:17px;color:var(--muted)}
.card .btn{left:60px;top:343px;width:145px;height:40px;font-size:12px}
.card.faded{opacity:.5}
.dots span{position:absolute;top:2666px;height:3px;width:40px;background:var(--line)}

/* who */
.who-title{left:113px;top:2808px;font-size:46px;line-height:1;color:var(--navy)}
.who-text{left:120px;top:2900px;width:510px;font-size:19.5px;line-height:26px;color:var(--ink)}

/* contact */
.contact-panel{left:134px;top:3410px;width:965px;height:565px;background:var(--navy);border-radius:0 0 70px 0}
.eyebrow{left:0;width:100%;top:58px;text-align:center;font-size:17px;letter-spacing:2px;color:var(--white)}
.contact-title{left:0;width:100%;top:88px;text-align:center;font-size:42px;line-height:1;color:var(--white)}
.contact-rule{left:440px;top:138px;width:78px;height:3px;background:var(--white)}
.field{position:absolute;background:var(--field);border-radius:2px;display:flex;align-items:flex-start;padding:15px 16px 0;gap:8px;font-size:15px;color:#4a4a5a}
.field svg{flex:none;margin-top:1px}

/* footer */
.footer-brand{left:0;width:1200px;top:4000px;display:flex;justify-content:center}
.footer-line{left:140px;width:920px;height:1px;background:rgba(255,255,255,.35)}
.footer-nav{left:0;width:1200px;top:4130px;display:flex;justify-content:center;gap:22px;align-items:center;font-family:"Rokkitt",serif;font-weight:700;font-size:17px;color:var(--white);text-transform:uppercase;white-space:nowrap}
.footer-nav i{width:4px;height:4px;border-radius:50%;background:var(--white);display:block}
.copyright{left:150px;top:4222px;font-size:15px;color:var(--white)}
.social{top:4212px;display:flex;gap:18px;left:918px}
.social span{width:22px;height:22px;border-radius:50%;border:2px solid var(--white)}
</style>
</head>
<body>

<!-- header -->
<header class="site-header abs">
  <div class="brand abs" style="left:95px;top:14px"><span class="brand-mark"></span>SnackHarbor</div>
  <nav class="main-nav">
    <a style="left:437px">About<br>SnackHarbor</a>
    <span class="sep" style="left:530px"></span>
    <a style="left:558px">Why Choose<br>SnackHarbor?</a>
    <span class="sep" style="left:667px"></span>
    <a style="left:695px">Products &amp;<br>Services</a>
    <span class="sep" style="left:796px"></span>
    <a style="left:823px">Contact<br>SnackHarbor</a>
  </nav>
  <div class="login abs">LOGIN</div>
</header>

<!-- hero -->
<section class="hero abs">
  <svg width="1200" height="680" viewBox="0 0 1200 680" class="abs" style="left:0;top:0">
    <defs>
      <linearGradient id="heroBg" x1="0" y1="0" x2="0" y2="1">
        <stop offset="0" stop-color="#1a1b55"/>
        <stop offset="0.55" stop-color="#2c3070"/>
        <stop offset="1" stop-color="#5a6490"/>
      </linearGradient>
    </defs>
    <path d="M0 0H1200V590C1120 585 1080 640 1000 650C930 660 900 600 820 600C720 600 660 670 560 670C470 670 440 590 340 590C250 590 200 650 120 660C70 665 30 620 0 600Z" fill="url(#heroBg)"/>
  </svg>
  <div role="img" aria-label="Northern Michigan harbor town at dusk behind the hero" class="abs" style="left:0;top:300px;width:600px;height:280px;background:linear-gradient(180deg,rgba(90,100,140,0) 0%,rgba(110,120,150,.35) 100%)"></div>
  <div role="img" aria-label="Close-up of a stocked vending machine inside a green ring" class="abs" style="left:600px;top:78px;width:510px;height:510px;border-radius:50%;border:9px solid var(--green);background:radial-gradient(circle at 45% 45%,#6a7a8a 0%,#3a4a5a 55%,#1e2a36 100%)"></div>
  <div role="img" aria-label="Front view of a snack vending machine" class="abs" style="left:597px;top:310px;width:188px;height:340px;border-radius:4px;background:linear-gradient(180deg,#2a2a2e 0%,#3b3a40 62%,#c9c9cc 63%,#e3e3e6 100%)"></div>
  <svg class="abs" style="left:550px;top:255px" width="62" height="36" viewBox="0 0 62 36"><path d="M2 14C18 2 40 4 56 26" fill="none" stroke="#fff" stroke-width="2"/><path d="M48 24L57 28L58 18" fill="none" stroke="#fff" stroke-width="2"/></svg>
</section>
<div class="hero-title heading abs">SnackHarbor</div>
<div class="hero-sub heading abs">Crave. Vend. Repeat</div>
<div class="hero-tag abs">Elevating snacking,<br>one vend at a time</div>
<div class="btn btn-green" style="left:107px;top:473px;width:197px;height:57px">Learn More</div>
<div class="btn btn-outline" style="left:318px;top:473px;width:198px;height:57px">View Products</div>

<!-- about -->
<svg class="abs" style="left:0;top:800px" width="590" height="560" viewBox="0 0 590 560">
  <path d="M0 40C150 40 300 -10 430 20C540 45 590 140 575 300C560 440 500 520 430 530L0 560Z" fill="var(--green)"/>
</svg>
<div role="img" aria-label="Woman smiling beside a drinks vending machine" class="abs" style="left:0;top:812px;width:568px;height:530px;border-radius:0 260px 240px 0 / 0 300px 230px 0;background:linear-gradient(120deg,#2b2f6a 0%,#4a5a86 35%,#9a8a78 70%,#5a4a3a 100%)"></div>
<div role="img" aria-label="Blue-fronted drinks vending machine" class="abs" style="left:55px;top:1078px;width:200px;height:290px;border-radius:3px;background:linear-gradient(180deg,#c8ccd6 0%,#5a7fc6 60%,#2a5ab8 100%)"></div>
<div class="about-title heading abs">About SnackHarbor</div>
<div class="about-text abs">At SnackHarbor, we don’t just vend snacks—we curate cravings. Our customized vending solutions bring flavor, convenience, and community to Northern Michigan. Whether you’re reaching for a mid-morning snack, a re-freshing beverage, or a satisfying breakfast burrito, SnackHarbor delivers delight with every bite</div>
<div class="btn btn-navy" style="left:631px;top:1177px;width:170px;height:49px;font-size:13px">Learn More</div>

<!-- why -->
<svg class="abs" style="left:0;top:1395px" width="1200" height="645" viewBox="0 0 1200 645">
  <defs>
    <linearGradient id="whyBg" x1="0" y1="0" x2="0" y2="1">
      <stop offset="0" stop-color="#2b5a2a"/>
      <stop offset="0.6" stop-color="#2f6236"/>
      <stop offset="1" stop-color="#3d6f4a"/>
    </linearGradient>
  </defs>
  <path d="M0 0H1200V560C1120 590 1050 640 960 630C860 620 800 560 680 570C560 580 470 640 360 630C250 620 180 570 100 572C60 573 20 580 0 585Z" fill="url(#whyBg)"/>
  <path d="M0 585C20 580 60 573 100 572C180 570 250 620 360 630" fill="none" stroke="var(--navy)" stroke-width="6"/>
</svg>
<div role="img" aria-label="Aerial view of green Northern Michigan forest and lake" class="abs" style="left:0;top:1640px;width:1200px;height:300px;background:linear-gradient(180deg,rgba(60,110,70,0) 0%,rgba(70,120,90,.4) 60%,rgba(60,100,80,0) 100%)"></div>
<div class="why-title heading abs">Why SnackHarbor ?</div>
<div class="why-rule abs"></div>
<div class="why-text abs">At SnackHarbor, we’re more than vending machines; we’re flavor architects, community connectors, and taste trailblazers. Imagine a world where every snack is an adventure, every sip a celebration. That’s the SnackHarbor promise—a symphony of taste, convenience, and camaraderie. Our Tailored Temptations await: from salty to sweet, our snack selection dances with variety.</div>
<div role="img" aria-label="Row of four vending machines: snacks, drinks, combo and coffee" class="abs" style="left:272px;top:1720px;width:672px;height:305px;border-radius:4px;background:linear-gradient(90deg,#3a3a40 0%,#2c2c32 25%,#34343a 50%,#2a2a30 75%,#1c1c20 100%)"></div>

<!-- products -->
<div class="products-title heading abs">Our Products!</div>
<div class="products-rule abs"></div>

<div class="card" style="left:93px">
  <div class="photo" role="img" aria-label="Drinks vending machine with blue base" style="background:linear-gradient(180deg,#9aa0b0 0%,#c0c6d2 60%,#2e6ad0 85%,#1e3a8a 100%)"></div>
  <h3>VENDOR MACHINE</h3>
  <p>Lorem ipsum dolor sit amet, consec-<br>tetur adipiscing elit sed d</p>
  <div class="btn btn-green">Learn More</div>
</div>
<div class="card" style="left:384px">
  <div class="photo" role="img" aria-label="Snack vending machine with blue side panel" style="background:linear-gradient(90deg,#3a3d4a 0%,#4a4e5e 70%,#3a78d0 100%)"></div>
  <h3>VENDOR MACHINE</h3>
  <p>Lorem ipsum dolor sit amet, consec-<br>tetur adipiscing elit sed d</p>
  <div class="btn btn-green">Learn More</div>
</div>
<div class="card" style="left:673px">
  <div class="photo" role="img" aria-label="Black combo vending machine" style="background:linear-gradient(180deg,#2a2c3a 0%,#3a3e5a 70%,#d8d8d0 72%,#e8e8e0 100%)"></div>
  <h3 style="top:270px">VENDOR MACHINE</h3>
  <p style="top:301px">Lorem ipsum dolor sit amet, consec-<br>tetur adipiscing elit sed d</p>
  <div class="btn btn-green" style="top:346px">Learn More</div>
</div>
<div class="card faded" style="left:963px;border-right:none;border-radius:12px 0 0 12px">
  <div class="photo" role="img" aria-label="Silver snack vending machine" style="background:linear-gradient(180deg,#7a7e8a 0%,#a8acb6 65%,#d8dae0 100%)"></div>
  <h3 style="top:270px">VENDOR MACHINE</h3>
  <p style="top:301px">Lorem ipsum dolor sit amet, consec-<br>tetur adipiscing elit sed d</p>
  <div class="btn btn-green" style="top:346px">Learn More</div>
</div>
<div class="dots"><span style="left:535px;background:var(--green)"></span><span style="left:587px"></span><span style="left:637px"></span></div>

<!-- who -->
<div role="img" aria-label="Faded view of a Northern Michigan town and hills" class="abs" style="left:0;top:3130px;width:1200px;height:780px;background:linear-gradient(180deg,rgba(255,255,255,0) 0%,rgba(200,206,200,.45) 40%,rgba(190,196,186,.5) 100%)"></div>
<svg class="abs" style="left:630px;top:2758px" width="570" height="520" viewBox="0 0 570 520">
  <path d="M110 20C230 -10 420 10 570 5V455C460 470 380 500 270 515C140 530 40 470 15 340C-10 200 20 60 110 20Z" fill="var(--green)"/>
</svg>
<div role="img" aria-label="Glass-front vending machines filled with snacks" class="abs" style="left:642px;top:2770px;width:558px;height:495px;border-radius:110px 0 0 200px / 60px 0 0 200px;background:linear-gradient(90deg,#1a1416 0%,#3a2a2a 30%,#2a1e20 55%,#4a2a22 80%,#2a1a16 100%)"></div>
<div class="who-title heading abs">Who We Are!</div>
<div class="who-text abs">
  <p>We’re not just about vending machines; we’re your culinary companions, your flavor curators,</p>
  <p style="margin-top:8px">and your secret stash of happiness.We’re the ones who believe that a vending machine isn’t just a metal box; it’s a portal to delight.</p>
  <p>Our mission? To transform mundane moments into memorable bites. Daniel and Nora, the dynamic duo behind SnackHarbor, have a passion for all things tasty. With backgrounds in sales and a penchant for personal connections, they’ve transformed the vending experience into an art form.</p>
</div>
<div class="btn btn-navy" style="left:120px;top:3211px;width:171px;height:50px;font-size:13px">Learn More</div>

<!-- footer band -->
<svg class="abs" style="left:0;top:3830px" width="1200" height="477" viewBox="0 0 1200 477">
  <path d="M0 80C150 40 300 30 600 40C900 30 1050 50 1200 20V477H0Z" fill="var(--green)"/>
</svg>

<!-- contact -->
<section class="contact-panel abs">
  <div class="eyebrow abs">GET IN TOUCH</div>
  <div class="contact-title heading abs">Contact Us!</div>
  <div class="contact-rule abs"></div>
  <div class="field" style="left:101px;top:170px;width:372px;height:50px">
    <svg width="14" height="14" viewBox="0 0 14 14"><circle cx="7" cy="4" r="3.2" fill="#9a9aa6"/><path d="M1 14C1 9 13 9 13 14Z" fill="#9a9aa6"/></svg>First Name</div>
  <div class="field" style="left:488px;top:170px;width:372px;height:50px">
    <svg width="14" height="14" viewBox="0 0 14 14"><circle cx="7" cy="4" r="3.2" fill="#9a9aa6"/><path d="M1 14C1 9 13 9 13 14Z" fill="#9a9aa6"/></svg>Last Name</div>
  <div class="field" style="left:101px;top:233px;width:372px;height:50px">
    <svg width="15" height="12" viewBox="0 0 15 12"><rect x="0.5" y="0.5" width="14" height="11" fill="#9a9aa6"/><path d="M1 1L7.5 6.5L14 1" fill="none" stroke="#fff" stroke-width="1.2"/></svg>Email address</div>
  <div class="field" style="left:488px;top:233px;width:372px;height:50px">
    <svg width="14" height="14" viewBox="0 0 14 14"><path d="M3 1L5.5 4L4 6C5 8 6 9 8 10L10 8.5L13 11L11.5 13C6 13 1 8 1 2.5Z" fill="#9a9aa6"/></svg>Phone</div>
  <div class="field" style="left:101px;top:300px;width:759px;height:128px">
    <svg width="14" height="13" viewBox="0 0 14 13"><ellipse cx="7" cy="5.5" rx="6.5" ry="5" fill="#9a9aa6"/><path d="M3 9L2 13L6 10Z" fill="#9a9aa6"/></svg>Message</div>
  <div class="btn btn-outline" style="left:382px;top:452px;width:210px;height:50px;font-size:15px">Send Message</div>
</section>

<!-- footer -->
<div class="footer-brand abs"><div class="brand" style="color:var(--white);font-size:48px"><span class="brand-mark" style="background:var(--white)"></span>SnackHarbor</div></div>
<div class="footer-line abs" style="top:4108px"></div>
<nav class="footer-nav abs">
  <span>Home</span><i></i><span>About SnackHarbor</span><i></i><span>Why Choose SnackHarbor?</span><i></i><span>Products &amp; Services</span><i></i><span>Contact Us</span>
</nav>
<div class="footer-line abs" style="top:4185px"></div>
<div class="copyright abs">Copyright © 2024 SnackHarbor. All rights reserved.</div>
<div class="social abs" aria-label="Social links"><span></span><span></span><span></span><span></span></div>

</body>
</html>
```